Non Propellant Static Eliminating Spray product needs a creative label design and logo

I need a label design that will speak for itself. I do not have a logo for the product name as it will just be part of the label design you come up with. The product is a static eliminating spray for all purpose use including hair, clothing, pets, all fabrics and can be used on just about anything. I would like to show somehow (maybe simple or line drawings of icons with staticy hair, pet, dress, pants ect.) Product name is "Crinkle Calm". This is my first product and only product as of right now. I will attach some info to maybe help with direction. I would like it to cater not only to the general public but to salons as well, if possible. I will need it to fit into the section where "Fiber Hush and laundry items are sold (picture attached). Although most of the coloring in this section is blues,reds,yellow and oranges I would like it to have a slight stand out of a pop to have your eyes gravitate to my product. I'm thinking possible a darker bright blue or dark brighter Aqua/Teal. (attached pic for reference of color) Doesn't have to be these colors though. I would like some form of mild background and something making you think of static and blocking of static if possible. This must appeal to women and men. More women but a percentage of men as well so not too feminine and not masculine. My product is made from natural and naturally derived ingredients & is made in the USA. The product is "Patent Pending" & have a UPC also product name is in for Trademark so I will need TM. I am in the process of searching for a new bottle as I feel I need to compete with what's on the shelves currently. I am looking at either a white or black 8oz bottle with either a white or black or colored (possibly metallic finger sprayer with a cap on that) I may be using an over cap. Pictures are attached to give you a general idea. 8 oz bottle circumference will be about 1 7/8" to 2". I will update as soon as I know. I will also be having a 2oz or 3oz travel size as well. This bottle will not have an over cap, it will only have a finger sprayer with cap.
I am excited to see what you can come up with. Please feel free to be creative outside of anything I submitted. I'm still kind of at a loss of what I want but will know it when I see it. Please don't hesitate to contact me with any questions. Thank you for your help and your time.
Marla

I have updated my contest prize, I wasn't able to do the prize amount that I originally wanted to when I submitted for the job. Also, here are some dimensions and descriptions that I have updated. The dimensions of the label will be about 5.125". Bottle is white with either a white pump sprayer or black sprayer with a clear cap. Bottle is 8oz & dimensions are Total Hght: 6.16", Base Diameter 2.01", Circumference 6.375". I am going to be doing one continuous label. I will also be needing the label for a 2oz bottle as well. Please let me know if you need dimensions for that. My product name is also in for trademark and will need to have TM on it. Thank you to all participants and I am excited to see what you come up with.Marla Added Monday, November 16, 2015

Target Market(s)

Linen Loft & More, Retail stores and Hair salons

Industry/Entity Type

Product

Requirements
Must have
• I will need some claims on the bottle. Hoping to be able to get a few on the front to let people know the benefits of my product going up against the only product on the market which has been around for 40 years but is not a good product at all.
• * Long Lasting
• * Non Flammable
• * Use on Hair, Clothes, Pets (maybe icons)
• * Natural & Naturally derived ingredients
• * All purpose Static Eliminator
• * Fresh Scent
Should not have
• Not a big fan of lightning rods or bolts unless mild enough to depict static. Fancy fonts.

```html
<!DOCTYPE html>
<html lang="en">
<head>
<meta charset="utf-8">
<title>Crinkle Calm – All Purpose Static Eliminator Label</title>
<link rel="stylesheet" href="https://fonts.googleapis.com/css2?family=Open+Sans:wght@600;700&family=Oswald:wght@400;500&display=swap">
<style>
  :root {
    --page-bg: #e6e6e6;
    --label-teal: #1e4a43;
    --label-teal-deep: #173d37;
    --ink-white: #ffffff;
    --ink-soft: #e4ece9;
    --rule: rgba(255, 255, 255, 0.55);
    --icon-fill: #dfe6e4;
  }
  * { box-sizing: border-box; margin: 0; padding: 0; }
  html, body {
    width: 667px;
    height: 1200px;
    overflow: hidden;
  }
  body {
    position: relative;
    background: var(--page-bg);
    font-family: "Open Sans", Arial, sans-serif;
    color: var(--ink-white);
  }
  .label {
    position: absolute;
    left: 190px;
    top: 258px;
    width: 287px;
    height: 852px;
    overflow: hidden;
    background: linear-gradient(90deg, var(--label-teal-deep) 0%, var(--label-teal) 30%, var(--label-teal) 70%, var(--label-teal-deep) 100%);
  }
  .label > * { position: absolute; left: 0; width: 100%; text-align: center; }

  .product-name {
    top: 80px;
    font-family: "Oswald", "Arial Narrow", sans-serif;
    font-weight: 500;
    font-size: 68px;
    line-height: 86px;
    letter-spacing: 1px;
    white-space: nowrap;
    text-transform: uppercase;
    transform: scaleY(1.4);
    transform-origin: top center;
  }
  .tm {
    font-size: 12px;
    vertical-align: top;
    line-height: 1;
    position: relative;
    top: 14px;
    margin-left: 2px;
  }

  .category-kicker {
    top: 353px;
    display: flex;
    align-items: center;
    justify-content: center;
    gap: 8px;
    font-size: 12.5px;
    font-weight: 600;
    letter-spacing: 0.6px;
    color: var(--ink-soft);
  }
  .category-kicker::before,
  .category-kicker::after {
    content: "";
    width: 46px;
    height: 1px;
    background: var(--rule);
  }
  .category-title {
    top: 374px;
    font-size: 19px;
    font-weight: 700;
    letter-spacing: 0.8px;
  }

  .uses-panel {
    top: 414px;
    left: 24px;
    width: 236px;
    height: 84px;
    border: 1.5px solid var(--rule);
    border-radius: 6px;
  }
  .uses-title {
    position: absolute;
    top: -9px;
    left: 50%;
    transform: translateX(-50%);
    padding: 0 6px;
    background: var(--label-teal);
    font-size: 10px;
    font-weight: 700;
    letter-spacing: 1.5px;
  }
  .uses-list {
    list-style: none;
    display: flex;
    justify-content: space-between;
    padding: 12px 10px 0;
  }
  .use-item {
    position: relative;
    width: 56px;
    height: 56px;
    border: 1.5px solid var(--ink-soft);
    border-radius: 50%;
    display: flex;
    align-items: center;
    justify-content: center;
  }
  .use-name {
    position: absolute;
    top: 5px;
    left: 0;
    width: 100%;
    text-align: center;
    font-size: 6.5px;
    font-weight: 700;
    letter-spacing: 0.5px;
  }
  .use-icon {
    margin-top: 8px;
    width: 34px;
    height: 30px;
    border-radius: 50%;
    background: var(--icon-fill);
  }

  .claims {
    top: 524px;
    list-style: none;
    font-size: 19.5px;
    font-weight: 600;
    line-height: 29px;
  }

  .fine-print {
    top: 664px;
    left: 28px;
    width: 231px;
    font-size: 9.6px;
    font-weight: 700;
    line-height: 13.5px;
  }
  .fine-rule {
    top: 737px;
    left: 56px;
    width: 175px;
    height: 1px;
    background: var(--rule);
  }
  .net-weight {
    top: 756px;
    font-family: "Oswald", "Arial Narrow", sans-serif;
    font-weight: 400;
    font-size: 20px;
    letter-spacing: 0.2px;
  }
</style>
</head>
<body>
  <main class="label">
    <h1 class="product-name">Crinkle<br>Calm<span class="tm">™</span></h1>

    <p class="category-kicker">ALL PURPOSE</p>
    <p class="category-title">STATIC ELIMINATOR</p>

    <section class="uses-panel">
      <h2 class="uses-title">USES</h2>
      <ul class="uses-list">
        <li class="use-item">
          <span class="use-name">HAIRS</span>
          <span class="use-icon" role="img" aria-label="Icon of a head with curly hair"></span>
        </li>
        <li class="use-item">
          <span class="use-name">CLOTHES</span>
          <span class="use-icon" role="img" aria-label="Icon of a shirt on a hanger"></span>
        </li>
        <li class="use-item">
          <span class="use-name">PETS</span>
          <span class="use-icon" role="img" aria-label="Icon of a dog and a cat"></span>
        </li>
      </ul>
    </section>

    <ul class="claims">
      <li>Long Lasting</li>
      <li>Non Flammable</li>
      <li>Natural Ingredients</li>
      <li>Fresh Scent</li>
    </ul>

    <p class="fine-print">Lorem ipsum dolor sit amet, consectetur adipisicing elit, sed do eiusmod tempor incididunt ut labore et dolore magna aliqua. Ut enim ad minim veniam, quis nostrud exercitation.</p>
    <div class="fine-rule"></div>

    <p class="net-weight">NET WT 8.2 OZ (186g)</p>
  </main>
</body>
</html>
```